Brindo like IOS/Android app for Okinawa Island - LumaTrail

LumaTrail is the name of the app
The closest thing that I can relate this app to is a region specific Brindo app. The app is for the island of Okinawa and is geared towards English speaking travelers. The style of app that I prefer is a look and feel similar to that of the new Nestora app, color should also be similar if not the same as the nestora app.

The app needs to have the following screens

LOGIN SCREEN
1. App login page with a login for chatterly button or create an account option. Personally I would like an image in the background with a real beachy feel, but don't do this if it messes with your design.

2. Depending on the choice of login there will need to be a second login screen to create the account. Nestora does this nicely.

PRIMARY HOME
primary page similar to the primary layout when you get into the nestora app.
This page is kind of like the home page of the app and should include the following items:
search field
upcoming events
popular things to do
featured restaurants
Featured Places to stay
area guides
Moving here
(this will allow the person to select, housing agencies, auto dealers, schools etc) These are essentially just quick searches.
Each selection should be listed so that the user can swipe to the left or right in order to view more listings under the categories listed above. It will not be the full list but rather a sample.

SIDEBAR POPOUT MENU
Popout sidebar that contains the following selections
Places to Eat
Things to do
Attractions
Beaches
Shop
Farmers Markets
Places to Stay
Schools & DayCare
Housing
Auto
Events
Account settings
Add a business

LIST VIEW
4. List view page for whatever category the user selected. This will show all the listings for the specific category: The top should also have the featured listings for that category

INDIVIDUAL LISTING
5. Listing page
This will include photos, description, hours, map(this can be a button to view the map or the map), Reviews with a leave a review option

AREA GUIDES
6. Area Guides. This is where the user will be able to select a specific area and learn about it. It should include an area where there can be a description, photos with a hero photo image, a map, popular local attractions or things to do, best restaurants in the area, places to stay etc.

PROFILE PAGE
7. Profile page for the user where they can make any updates they need to

Every page but the listing page should include the search bar. When the user clicks in it they should be able to see a drop down of quick select searches or run a regular search.

Logo
I have attached a logo that was made that needs a redesign. The map marker contains the logo for Okinawa within it so it does need to be similar.

If you have any questions or need clarification please send me a message. I will respond promptly.
Thank you,

```html
<!DOCTYPE html>
<html lang="en">
<head>
<meta charset="utf-8">
<title>LumaTrail – Home</title>
<link rel="stylesheet" href="https://fonts.googleapis.com/css2?family=Mulish:wght@300;400;600&display=swap">
<style>
  :root {
    --coral: #f88282;
    --tile: #8fb4e8;
    --white: #ffffff;
    --ink: #111111;
    --icon-grey: #8a8a8a;
    --divider: #dcdcdc;
  }
  * { box-sizing: border-box; margin: 0; padding: 0; }
  html, body { width: 675px; height: 1200px; overflow: hidden; background: var(--white); }
  body { font-family: "Mulish", "Helvetica Neue", Arial, sans-serif; }

  .app-screen { position: relative; width: 675px; height: 1200px; overflow: hidden; background: var(--white); }

  .top-bar { position: absolute; left: 0; top: 0; width: 675px; height: 162px; background: var(--coral); }

  .status-bar { position: absolute; left: 0; top: 0; width: 100%; height: 36px; font-size: 21px; color: var(--ink); }
  .status-bar .carrier { position: absolute; left: 10px; top: 6px; display: flex; align-items: center; gap: 8px; }
  .status-bar .signal { display: flex; gap: 3px; }
  .status-bar .signal span { width: 9px; height: 9px; border-radius: 50%; background: var(--ink); }
  .status-bar .clock { position: absolute; left: 0; right: 0; top: 6px; text-align: center; font-weight: 600; }
  .status-bar .battery { position: absolute; right: 12px; top: 6px; display: flex; align-items: center; gap: 6px; }
  .battery-cell { width: 42px; height: 19px; border: 2px solid var(--ink); border-radius: 4px; padding: 2px; position: relative; }
  .battery-cell::before { content: ""; display: block; width: 100%; height: 100%; background: var(--ink); border-radius: 1px; }
  .battery-cell::after { content: ""; position: absolute; right: -6px; top: 5px; width: 3px; height: 6px; background: var(--ink); border-radius: 0 2px 2px 0; }

  .menu-button { position: absolute; left: 29px; top: 70px; width: 57px; height: 26px; }
  .menu-button span { position: absolute; left: 0; height: 3px; background: var(--white); border-radius: 2px; }
  .menu-button span:nth-child(1) { top: 0; width: 57px; }
  .menu-button span:nth-child(2) { top: 11px; width: 40px; }
  .menu-button span:nth-child(3) { top: 22px; width: 57px; }

  .app-title { position: absolute; left: 0; right: 0; top: 58px; text-align: center; color: var(--white); font-size: 40px; font-weight: 300; letter-spacing: 0.5px; }

  .search-button { position: absolute; left: 591px; top: 61px; width: 50px; height: 50px; }

  .category-grid { position: absolute; left: 29px; top: 211px; width: 617px; display: grid; grid-template-columns: 295px 295px; column-gap: 27px; row-gap: 28px; list-style: none; }
  .category-tile { height: 252px; background: var(--tile); color: var(--white); display: flex; flex-direction: column; align-items: center; justify-content: flex-start; padding-top: 52px; }
  .category-tile svg, .category-tile .icon-slot { width: 100px; height: 100px; flex: none; }
  .category-label { font-size: 35px; font-weight: 400; line-height: 1.2; text-align: center; margin-top: 18px; }
  .category-label.two-line { margin-top: 8px; line-height: 1.18; }
  .icon-slot { border-radius: 40px 40px 14px 14px; background: rgba(255,255,255,0.22); }

  .tab-bar { position: absolute; left: 0; bottom: 0; width: 675px; height: 98px; border-top: 2px solid var(--divider); display: flex; }
  .tab-bar svg { position: absolute; top: 20px; width: 56px; height: 56px; }
</style>
</head>
<body>
<main class="app-screen">
  <header class="top-bar">
    <div class="status-bar">
      <div class="carrier">
        <div class="signal"><span></span><span></span><span></span><span></span><span></span></div>
        <span>Relay</span>
        <svg width="24" height="18" viewBox="0 0 24 18" aria-hidden="true"><path d="M2 6a14 14 0 0 1 20 0M5.5 9.5a9 9 0 0 1 13 0M9 13a4 4 0 0 1 6 0" fill="none" stroke="#111" stroke-width="2.4" stroke-linecap="round"/><circle cx="12" cy="16" r="1.6" fill="#111"/></svg>
      </div>
      <div class="clock">9:41 AM</div>
      <div class="battery"><span>100%</span><div class="battery-cell"></div></div>
    </div>
    <div class="menu-button" aria-label="Open menu"><span></span><span></span><span></span></div>
    <h1 class="app-title">LumaTrail</h1>
    <svg class="search-button" viewBox="0 0 50 50" aria-label="Search">
      <circle cx="25" cy="25" r="25" fill="var(--white)"/>
      <circle cx="23" cy="23" r="8" fill="none" stroke="var(--coral)" stroke-width="3.6"/>
      <line x1="29" y1="29" x2="34" y2="34" stroke="var(--coral)" stroke-width="4" stroke-linecap="round"/>
    </svg>
  </header>

  <ul class="category-grid">
    <li class="category-tile">
      <svg viewBox="0 0 100 100" fill="none" stroke="#fff" stroke-width="3.4" stroke-linecap="round" stroke-linejoin="round" aria-hidden="true">
        <path d="M10 44c0-20 18-32 40-32s40 12 40 32z"/>
        <g fill="#fff" stroke="none"><circle cx="36" cy="24" r="2"/><circle cx="50" cy="20" r="2"/><circle cx="64" cy="24" r="2"/><circle cx="28" cy="34" r="2"/><circle cx="43" cy="31" r="2"/><circle cx="57" cy="31" r="2"/><circle cx="72" cy="34" r="2"/></g>
        <path d="M10 56h80"/><path d="M10 67h80"/>
        <path d="M10 78h80v4c0 6-4 10-10 10H20c-6 0-10-4-10-10z"/>
      </svg>
      <span class="category-label">Eat</span>
    </li>
    <li class="category-tile">
      <svg viewBox="0 0 100 100" fill="none" stroke="#fff" stroke-width="3.4" stroke-linecap="round" stroke-linejoin="round" aria-hidden="true">
        <path d="M14 32c8-20 40-30 66-16z"/>
        <path d="M30 26l10 4M48 20l6 8M64 16l2 8"/>
        <path d="M46 27L36 70"/>
        <path d="M12 60c10 6 24 10 36 10l34 4"/>
        <path d="M20 74c16 4 40 6 60 6"/>
        <path d="M14 90c20-4 44-4 76 0"/>
      </svg>
      <span class="category-label">Beaches</span>
    </li>
    <li class="category-tile">
      <div class="icon-slot" role="img" aria-label="Attractions icon: local island figure"></div>
      <span class="category-label">Attractions</span>
    </li>
    <li class="category-tile">
      <svg viewBox="0 0 100 100" fill="none" stroke="#fff" stroke-width="3.4" stroke-linecap="round" stroke-linejoin="round" aria-hidden="true">
        <path d="M4 8h10l6 10h76l-12 50H26L20 18"/>
        <path d="M26 68l-4 10h66"/>
        <circle cx="32" cy="88" r="5"/><circle cx="78" cy="88" r="5"/>
      </svg>
      <span class="category-label">Shop</span>
    </li>
    <li class="category-tile">
      <svg viewBox="0 0 100 100" fill="none" stroke="#fff" stroke-width="3.4" stroke-linecap="round" stroke-linejoin="round" aria-hidden="true">
        <path d="M74 28c-14-8-34 0-46 18C18 62 12 80 14 86c6 2 24-4 40-16 18-14 26-30 20-42z"/>
        <path d="M40 40l6 6M30 56l6 5M52 58l-4-5M42 70l-4-4"/>
        <path d="M72 26c0-10 4-18 10-22M76 30c8-2 14-2 20 2M74 28c6-6 12-8 18-8"/>
      </svg>
      <span class="category-label two-line">Farmers<br>Markets</span>
    </li>
    <li class="category-tile">
      <svg viewBox="0 0 100 100" fill="none" stroke="#fff" stroke-width="3.4" stroke-linecap="round" stroke-linejoin="round" aria-hidden="true">
        <path d="M26 44V12h48v32"/>
        <path d="M34 44V22h32v22"/>
        <path d="M8 44h84v26H8z"/>
        <path d="M8 56h84"/>
        <path d="M14 70v14M86 70v14M14 84h72"/>
      </svg>
      <span class="category-label">Hotels</span>
    </li>
  </ul>

  <nav class="tab-bar" aria-label="Main tabs">
    <svg style="left:26px" viewBox="0 0 56 56" fill="none" stroke="var(--icon-grey)" stroke-width="2.6" stroke-linejoin="round" aria-label="Home">
      <path d="M4 26L28 5l24 21"/><path d="M10 21v31h36V21"/><path d="M22 52V34h12v18"/>
    </svg>
    <svg style="left:206px" viewBox="0 0 56 56" fill="none" stroke="var(--icon-grey)" stroke-width="2.6" aria-label="Map">
      <path d="M28 54s-17-20-17-33a17 17 0 0 1 34 0c0 13-17 33-17 33z"/><circle cx="28" cy="21" r="7"/>
    </svg>
    <svg style="left:411px" viewBox="0 0 56 56" fill="none" stroke="var(--icon-grey)" stroke-width="2.6" stroke-linejoin="round" aria-label="Saved">
      <path d="M28 48L8 28a11 11 0 0 1 20-14 11 11 0 0 1 20 14z"/>
    </svg>
    <svg style="left:591px" viewBox="0 0 56 56" fill="none" stroke="var(--icon-grey)" stroke-width="2.6" aria-label="Profile">
      <circle cx="28" cy="28" r="25"/><circle cx="28" cy="22" r="8"/><path d="M14 45c3-8 8-11 14-11s11 3 14 11"/>
    </svg>
  </nav>
</main>
</body>
</html>
```